KORVa: AI driven decarbonization application

We are seeking an engaging, user-friendly, and visually appealing user interface for our B2B SaaS platform, Brelmont KORVa. This solution helps large organizations achieve net-zero emissions using AI-driven forecasting, AI models, a emission mitigation library, and a scenario simulator..

A big challenge is to allow the user to work efficiently with multidimensional data.

Requirements:

* Design a modern, professional, and visually striking user interface, catering to a diverse audience within large corporations, including executives, strategists, and environmental specialists.

* Construct an intuitive navigation system, allowing users to seamlessly access functionalities for informed decision-making and tracking progress towards net-zero emissions.

* The application is expected to be used on desktops first

* Incorporate our brand's colors, and visual elements into the design to maintain consistency throughout the application.

* Provide design assets and documentation, such as style guides, design specifications, and necessary assets (e.g., icons, illustrations) for our development team to implement the design. We use Figma and would appreciate delivery as figma files.

Please note that we also need more pages over time. The most important is to get the work bench page right. We will also need:
* a landing page where the users can select previous scenarios and see some high level data.
* A page with information on historical data per asset
* An analytics page
* User and system administration pages.
These pages are out of scope for this project, but they should be available in the navigation solution.

Please submit your initial design concepts, accompanied by a brief explanation of your approach and the rationale behind your design choices. We will offer feedback and collaborate with the chosen designer to refine the design, ensuring it meets our requirements and vision.

We are really hoping to see some elegant user interfaces. The functionality describe in the attachment is important, but the layout is not. Feel free to invent.

Attached files:

Target Market(s)

Energy intensive industries

Requirements
Must have
• Easy to navigate through the different data dimensions: Time, assets, mitigation measures, and advanced details under mitigation measures. The design in the attached files are just our working drafts. Creative alternatives are very welcome.
Nice to have
• Elegant layouts that differ from our working drafts.

```html
<!DOCTYPE html>
<html lang="en">
<head>
<meta charset="utf-8">
<title>Brelmont KORVa – Scenario Simulation</title>
<link href="https://fonts.googleapis.com/css2?family=Montserrat:wght@400;500;600&display=swap" rel="stylesheet">
<style>
:root{
  --page:#313c82;
  --panel:#28316f;
  --sidebar:#28306b;
  --sidebar-deep:#1d2352;
  --row:#2f3978;
  --text:#ffffff;
  --muted:#bfc6ee;
  --dim:#8f98cf;
  --green:#47d4a6;
  --chip:#aab3e6;
  --chart-bg:#2e3776;
  --chart-future:#3a4483;
  --yellow:#f1ef73;
  --cyan:#36c2d0;
  --pink:#f08ac8;
}
*{box-sizing:border-box;margin:0;padding:0}
html,body{width:1200px;height:670px;overflow:hidden}
body{background:var(--page);font-family:'Montserrat',sans-serif;color:var(--text);position:relative}
.abs{position:absolute}

/* sidebar */
.sidebar{left:0;top:0;width:156px;height:670px;background:linear-gradient(180deg,var(--sidebar),var(--sidebar-deep))}
.brand{left:0;top:0;width:156px;height:60px;background:linear-gradient(135deg,#38d6a0,#9fe38a);display:flex;align-items:center;justify-content:center;gap:6px}
.brand-dot{width:8px;height:8px;border-radius:50%;background:#fff}
.brand-name{font-size:17px;font-weight:500;letter-spacing:1px;color:#fff}
.search{left:5px;top:75px;width:143px;height:17px;border:1px solid var(--green);border-radius:2px}
.search svg{position:absolute;right:4px;top:3px}
.menu{list-style:none;top:113px;left:0;width:156px}
.menu li{height:18.75px;line-height:18.75px;font-size:9px;color:var(--muted);position:relative;white-space:nowrap}
.menu .top{padding-left:18px}
.menu .top::before{content:"";position:absolute;left:9px;top:7px;width:4px;height:4px;border-right:1px solid var(--dim);border-bottom:1px solid var(--dim);transform:rotate(-45deg)}
.menu .top.open::before{transform:rotate(45deg);top:5px}
.menu .sub{padding-left:28px}
.menu .sub::before{content:"";position:absolute;left:21px;top:0;bottom:0;border-left:1px solid #47508c}
.menu .active{background:var(--green);color:#1f2a5c}

/* top nav */
.nav a{position:absolute;font-size:15px;color:var(--muted);text-decoration:none;white-space:nowrap}
.nav .current{color:#fff}
.user{top:17px;right:72px;text-align:center;font-size:11px;color:var(--muted);line-height:1.2}
.user small{font-size:9px;display:block}
.avatar{top:17px;left:1144px}

/* panels */
.panel{background:var(--panel)}
.panel-title{font-size:15px;font-weight:500;text-align:center}
.section-title{font-size:11px;font-weight:500;text-align:center}
.th{font-size:8.5px;font-weight:500}
.sh{font-size:5.5px;color:var(--muted)}
.td{font-size:7.5px;color:var(--muted);white-space:nowrap}
.status{width:12px;height:12px;border-radius:2px}
.st-green{background:linear-gradient(135deg,#5bd89a,#a6e07a)}
.st-grey{background:#b7bde6}
.param{font-size:8.5px;font-weight:500}
.chip{width:77px;height:14px;border-radius:2px;background:var(--chip);color:#2a3270;font-size:7px;text-align:center;line-height:14px}

/* timeline */
.ctrl{height:23px;background:#3a4485;border-radius:2px;display:flex;align-items:center;justify-content:center}
.date-select{font-size:9px;gap:8px}
.tl-label{font-size:8.5px;color:var(--muted);white-space:nowrap;transform:translateX(-50%)}
.track{left:169px;width:1017px;height:27px;background:var(--row)}
.bar{height:23px;border-radius:1px;padding:3px 12px 0;font-size:0}
.bar b{display:block;font-size:8.5px;font-weight:500;line-height:10px;white-space:nowrap}
.bar .sub{display:block;font-size:5.5px;line-height:7px;white-space:nowrap}
.bar .handle{position:absolute;right:6px;top:3px;width:17px;height:17px;border:1px solid rgba(255,255,255,.8);border-radius:2px;background:rgba(255,255,255,.12);display:flex;align-items:center;justify-content:center}
.g1{background:linear-gradient(90deg,#38d2b0,#a8e07a)}
.g2{background:linear-gradient(90deg,#c33fd8,#d98c7c)}
.g3{background:linear-gradient(90deg,#a14af0,#58a9f5)}
.g4{background:linear-gradient(90deg,#6669f2,#c47ff0)}
.g5{background:linear-gradient(90deg,#c041d1,#3dd3b0)}
.g6{background:linear-gradient(90deg,#5a9ff6,#bde27a)}
.included{font-size:8.5px;color:var(--muted)}
.volume{left:156px;top:628px;width:1044px;height:42px;background:linear-gradient(90deg,#e39a7c,#d07aa8 50%,#c33fd6);border-radius:40px 0 0 0}
</style>
</head>
<body>

<aside class="abs sidebar">
  <div class="abs brand"><span class="brand-dot"></span><span class="brand-name">BRELMONT</span></div>
  <div class="abs search">
    <svg width="10" height="10" viewBox="0 0 10 10"><circle cx="4" cy="4" r="3" fill="none" stroke="#47d4a6" stroke-width="1.2"/><line x1="6.2" y1="6.2" x2="9.5" y2="9.5" stroke="#47d4a6" stroke-width="1.4"/></svg>
  </div>
  <ul class="abs menu">
    <li class="top">Switch Energy Carrier</li>
    <li class="top open">Energy efficience measures</li>
    <li class="sub">Venting to flare</li>
    <li class="sub">Venting to production</li>
    <li class="sub">Fugitive emission measure</li>
    <li class="sub active">Compressor replacement</li>
    <li class="sub">Reduced water injection</li>
    <li class="sub">Reduced gas injection</li>
    <li class="sub">Drilling improveents</li>
    <li class="top">End of pipe measures</li>
    <li class="top open">Compray structure</li>
    <li class="sub">Change end of life</li>
    <li class="sub">New net zero assets</li>
    <li class="sub">Update license ownerships</li>
    <li class="top">Logistics</li>
    <li class="top">Carbon offsets</li>
  </ul>
</aside>

<nav class="abs nav" style="left:0;top:20px">
  <a style="left:302px">Home</a>
  <a style="left:389px">Assets</a>
  <a class="current" style="left:478px">Scenario Simulation</a>
  <a style="left:672px">Map</a>
</nav>
<div class="abs user">Random Name<small>My Computer</small></div>
<svg class="abs avatar" width="24" height="24" viewBox="0 0 24 24"><circle cx="12" cy="12" r="12" fill="#c6cbee"/><circle cx="12" cy="9" r="4.2" fill="#313c82"/><path d="M4.5 19.5c1.6-3.6 4.4-5 7.5-5s5.9 1.4 7.5 5" fill="#313c82"/></svg>

<section class="abs panel" style="left:163px;top:58px;width:496px;height:289px">
  <h2 class="abs panel-title" style="left:0;width:500px;top:16px">Power from shore</h2>
  <h3 class="abs section-title" style="left:0;width:300px;top:53px">Assets</h3>
  <h3 class="abs section-title" style="left:352px;width:100px;top:53px">Parameters</h3>

  <div class="abs th" style="left:9px;top:76px">Active filters:</div>
  <div class="abs th" style="left:75px;top:76px">Name</div>
  <div class="abs th" style="left:142px;top:76px">Ownership</div>
  <div class="abs th" style="left:226px;top:76px">Status</div>
  <div class="abs sh" style="left:9px;top:93px">Lorem</div>
  <div class="abs sh" style="left:75px;top:93px">Type</div>
  <div class="abs sh" style="left:106px;top:93px">Country</div>
  <div class="abs sh" style="left:143px;top:93px">Title</div>
  <div class="abs sh" style="left:227px;top:93px">Percent</div>
  <div class="abs sh" style="left:276px;top:93px">Status</div>

  <div class="abs td" style="left:9px;top:113px;line-height:19px">DEVG PVL D-5<br>DEVG PVL D-5<br>DEVG PVL D-5<br>DEVG PVL D-5<br>DEVG PVL D-5<br>DEVG PVL D-5<br>DEVG PVL D-5<br>DEVG PVL D-5<br>DEVG PVL D-5</div>
  <div class="abs td" style="left:76px;top:113px;line-height:19px">Field<br>Field<br>Field<br>Field<br>Field<br>Field<br>Field<br>Field<br>Field</div>
  <div class="abs td" style="left:114px;top:113px;line-height:19px">UK<br>UK<br>UK<br>UK<br>UK<br>UK<br>UK<br>UK<br>UK</div>
  <div class="abs td" style="left:143px;top:113px;line-height:19px">Marrow of Fenlay<br>Marrow of Fenlay<br>Marrow of Fenlay<br>Marrow of Fenlay<br>Marrow of Fenlay<br>Marrow of Fenlay<br>Marrow of Fenlay<br>Marrow of Fenlay<br>Marrow of Fenlay</div>
  <div class="abs td" style="left:228px;top:113px;line-height:19px">100%<br>100%<br>100%<br>100%<br>100%<br>100%<br>100%<br>100%<br>100%</div>
  <div class="abs td" style="left:257px;top:113px;line-height:19px">Producing<br>Producing<br>Producing<br>Producing<br>Producing<br>Producing<br>Producing<br>Producing<br>Producing</div>
  <div class="abs" style="left:303px;top:116px;display:flex;flex-direction:column;gap:7px">
    <span class="status st-green"></span><span class="status st-green"></span><span class="status st-green"></span>
    <span class="status st-green"></span><span class="status st-green"></span><span class="status st-grey"></span>
    <span class="status st-grey"></span><span class="status st-grey"></span><span class="status st-green"></span>
  </div>

  <div class="abs param" style="left:348px;top:77px;line-height:19px">Start<br>End<br>Duration<br>Factor<br>Jalla Jalla</div>
  <div class="abs chip" style="left:406px;top:74px">January 2023</div>
  <div class="abs chip" style="left:406px;top:93px">October 2024</div>
  <div class="abs chip" style="left:406px;top:112px">21 months</div>
  <div class="abs chip" style="left:406px;top:130px">2 x</div>
  <span class="abs status st-green" style="left:468px;top:149px;width:14px;height:14px"></span>
</section>

<section class="abs panel" style="left:669px;top:59px;width:522px;height:288px">
  <h2 class="abs panel-title" style="left:0;width:522px;top:15px">Predicted specific CO₂ emissions</h2>
  <svg class="abs" style="left:0;top:0" width="522" height="288" viewBox="0 0 522 288" role="img" aria-label="Line chart of predicted specific CO2 emissions 1995 to 2050">
    <rect x="50" y="52" width="442" height="192" fill="#2c3572"/>
    <rect x="271" y="52" width="221" height="192" fill="#3a4483" opacity=".55"/>
    <g font-family="Montserrat,sans-serif" font-size="8.5" fill="#7fa0ff">
      <text x="41" y="56" text-anchor="end">175</text>
      <text x="41" y="83" text-anchor="end">150</text>
      <text x="41" y="111" text-anchor="end">125</text>
      <text x="41" y="138" text-anchor="end">100</text>
      <text x="41" y="165" text-anchor="end">75</text>
      <text x="41" y="192" text-anchor="end">50</text>
      <text x="41" y="220" text-anchor="end">25</text>
      <text x="34" y="247" text-anchor="end">0</text>
      <text x="59" y="256" text-anchor="middle">1995</text>
      <text x="96" y="256" text-anchor="middle">2000</text>
      <text x="135" y="256" text-anchor="middle">2005</text>
      <text x="172" y="256" text-anchor="middle">2010</text>
      <text x="211" y="256" text-anchor="middle">2015</text>
      <text x="247" y="256" text-anchor="middle">2020</text>
      <text x="288" y="256" text-anchor="middle">2025</text>
      <text x="327" y="256" text-anchor="middle">2030</text>
      <text x="367" y="256" text-anchor="middle">2035</text>
      <text x="406" y="256" text-anchor="middle">2040</text>
      <text x="445" y="256" text-anchor="middle">2045</text>
      <text x="483" y="256" text-anchor="middle">2050</text>
    </g>
    <polyline fill="none" stroke="#f08ac8" stroke-width="1.3" points="267,167 299,167 315,186 331,192 355,184 379,200 411.6,214 436,210 460,224 492,226"/>
    <polyline fill="none" stroke="#36c2d0" stroke-width="1.6" points="250.9,161.7 275,172.7 299,180 331,190 371,198 411.6,206 452,215 492,228"/>
    <polyline fill="none" stroke="#f1ef73" stroke-width="1.2" stroke-linejoin="round" points="50,222 54,235 58,233 60,218 62,216.6 64,236 66.1,230.8 68,200 70.1,172.7 72,235 74.1,227.5 78,232 82.1,222.1 86,234 90.2,230.8 94,225 98.2,211.1 102,200 106.3,191.3 110,196 114.3,200.1 118,184 122.3,186.9 126,198 130.4,194.6 134,180 138.4,167.2 140,192 142.4,189.1 146.4,183.7 150,172 154.5,176 158,190 162.5,189.1 166,175 170.5,172.7 174,160 178.6,158.4 182,170 186.6,167.2 190,148 194.6,150.7 198,165 202.7,156.2 206,140 210.7,123.3 212,160 214.7,167.2 216,130 218.8,106.9 220,150 222.8,167.2 224,140 226.8,147.5 230,170 234.8,161.7 238,145 242.9,154 246,172 250.9,165 254,150 258.9,156.2 262,170 267,167.2 270,155 275,161.7 279,172 283,167.2 287,160 291.1,165 299,162 307.2,158.4 315,160 323,155 331.3,154 339,153 347.3,150.7 355,152 363,146 371.4,145.3 379,142 387.5,134.3 391,140 395.5,139.8 403,128 411.6,117.8 419,114 427.7,106.9 431,104 435.7,101.4 443,105 451.8,101.4 459,92 467.8,84.9 475,76 483,68 492,55.3"/>
    <g font-family="Montserrat,sans-serif" font-size="8.5" fill="#7fa0ff">
      <circle cx="76" cy="271" r="3" fill="#f1ef73"/><text x="87" y="274">Corporate average</text>
      <circle cx="199" cy="271" r="3" fill="#36c2d0"/><text x="210" y="274">Corporate goals</text>
      <circle cx="311" cy="271" r="3" fill="#f08ac8"/><text x="322" y="274">Corporate average incl measures</text>
    </g>
  </svg>
</section>

<section class="abs panel" style="left:163px;top:356px;width:1028px;height:245px"></section>
<h2 class="abs panel-title" style="left:560px;width:236px;top:367px">Power from shore</h2>
<div class="abs included" style="left:1031px;top:373px">7/10 Assets included</div>
<div class="abs ctrl" style="left:1140px;top:365px;width:24px;height:24px">
  <svg width="12" height="16" viewBox="0 0 12 16"><path d="M6 1v14M3 4l3-3 3 3M3 12l3 3 3-3M1 8h10" stroke="#fff" fill="none" stroke-width="1"/></svg>
</div>

<div class="abs ctrl" style="left:169px;top:391px;width:25px"><svg width="14" height="8" viewBox="0 0 14 8"><path d="M7 0L0 4l7 4zM14 0L7 4l7 4z" fill="#c9cff0"/></svg></div>
<div class="abs ctrl" style="left:199px;top:391px;width:22px"><svg width="8" height="9" viewBox="0 0 8 9"><path d="M0 0l8 4.5L0 9z" fill="#c9cff0"/></svg></div>
<div class="abs ctrl" style="left:227px;top:391px;width:25px"><svg width="14" height="8" viewBox="0 0 14 8"><path d="M0 0l7 4-7 4zM7 0l7 4-7 4z" fill="#c9cff0"/></svg></div>
<div class="abs ctrl date-select" style="left:258px;top:391px;width:90px">January 2023 <svg width="7" height="5" viewBox="0 0 7 5"><path d="M0 0h7L3.5 5z" fill="#c9cff0"/></svg></div>

<div class="abs tl-label" style="left:420px;top:393px">January 2023</div>
<div class="abs tl-label" style="left:511px;top:393px">July 2023</div>
<div class="abs tl-label" style="left:587px;top:393px">January 2024</div>
<div class="abs tl-label" style="left:678px;top:393px">July 2024</div>
<div class="abs tl-label" style="left:751px;top:393px">January 2025</div>
<div class="abs tl-label" style="left:840px;top:393px">July 2025</div>
<div class="abs tl-label" style="left:918px;top:393px">January 2026</div>
<div class="abs tl-label" style="left:1009px;top:393px">July 2026</div>
<div class="abs tl-label" style="left:1084px;top:393px">January 2027</div>
<div class="abs tl-label" style="left:1169px;top:393px">July 2027</div>

<svg class="abs" style="left:354px;top:404px" width="828" height="10" viewBox="0 0 828 10" aria-hidden="true">
  <line x1="0" y1="9" x2="826" y2="9" stroke="#c9cff0" stroke-width="1"/>
  <g stroke="#c9cff0" stroke-width="1">
    <line x1="0.5" y1="1" x2="0.5" y2="9"/><line x1="14" y1="5" x2="14" y2="9"/><line x1="28" y1="5" x2="28" y2="9"/><line x1="42" y1="5" x2="42" y2="9"/><line x1="55" y1="5" x2="55" y2="9"/><line x1="69" y1="5" x2="69" y2="9"/>
    <line x1="83" y1="1" x2="83" y2="9"/><line x1="97" y1="5" x2="97" y2="9"/><line x1="111" y1="5" x2="111" y2="9"/><line x1="125" y1="5" x2="125" y2="9"/><line x1="138" y1="5" x2="138" y2="9"/><line x1="152" y1="5" x2="152" y2="9"/>
    <line x1="166" y1="1" x2="166" y2="9"/><line x1="180" y1="5" x2="180" y2="9"/><line x1="194" y1="5" x2="194" y2="9"/><line x1="208" y1="5" x2="208" y2="9"/><line x1="221" y1="5" x2="221" y2="9"/><line x1="235" y1="5" x2="235" y2="9"/>
    <line x1="249" y1="1" x2="249" y2="9"/><line x1="263" y1="5" x2="263" y2="9"/><line x1="277" y1="5" x2="277" y2="9"/><line x1="291" y1="5" x2="291" y2="9"/><line x1="304" y1="5" x2="304" y2="9"/><line x1="318" y1="5" x2="318" y2="9"/>
    <line x1="332" y1="1" x2="332" y2="9"/><line x1="346" y1="5" x2="346" y2="9"/><line x1="360" y1="5" x2="360" y2="9"/><line x1="374" y1="5" x2="374" y2="9"/><line x1="387" y1="5" x2="387" y2="9"/><line x1="401" y1="5" x2="401" y2="9"/>
    <line x1="415" y1="1" x2="415" y2="9"/><line x1="429" y1="5" x2="429" y2="9"/><line x1="443" y1="5" x2="443" y2="9"/><line x1="457" y1="5" x2="457" y2="9"/><line x1="470" y1="5" x2="470" y2="9"/><line x1="484" y1="5" x2="484" y2="9"/>
    <line x1="498" y1="1" x2="498" y2="9"/><line x1="512" y1="5" x2="512" y2="9"/><line x1="526" y1="5" x2="526" y2="9"/><line x1="540" y1="5" x2="540" y2="9"/><line x1="553" y1="5" x2="553" y2="9"/><line x1="567" y1="5" x2="567" y2="9"/>
    <line x1="581" y1="1" x2="581" y2="9"/><line x1="595" y1="5" x2="595" y2="9"/><line x1="609" y1="5" x2="609" y2="9"/><line x1="623" y1="5" x2="623" y2="9"/><line x1="636" y1="5" x2="636" y2="9"/><line x1="650" y1="5" x2="650" y2="9"/>
    <line x1="664" y1="1" x2="664" y2="9"/><line x1="678" y1="5" x2="678" y2="9"/><line x1="692" y1="5" x2="692" y2="9"/><line x1="706" y1="5" x2="706" y2="9"/><line x1="719" y1="5" x2="719" y2="9"/><line x1="733" y1="5" x2="733" y2="9"/>
    <line x1="747" y1="1" x2="747" y2="9"/><line x1="761" y1="5" x2="761" y2="9"/><line x1="775" y1="5" x2="775" y2="9"/><line x1="789" y1="5" x2="789" y2="9"/><line x1="802" y1="5" x2="802" y2="9"/><line x1="826" y1="1" x2="826" y2="9"/>
  </g>
</svg>

<div class="abs track" style="top:422px"></div>
<div class="abs track" style="top:452px"></div>
<div class="abs track" style="top:481px"></div>
<div class="abs track" style="top:511px"></div>
<div class="abs track" style="top:541px"></div>
<div class="abs track" style="top:570px"></div>

<div class="abs bar g1" style="left:677px;top:424px;width:290px"><b>Compressor rebundling</b><span class="sub">3/10 Assets included</span><i class="handle"><svg width="7" height="11" viewBox="0 0 7 11"><path d="M3.5 0.5v10M1 3l2.5-2.5L6 3M1 8l2.5 2.5L6 8" stroke="#fff" fill="none"/></svg></i></div>
<div class="abs bar g2" style="left:486px;top:454px;width:392px"><b>Optimize gas lift</b><span class="sub">5/10 Assets included</span><i class="handle"><svg width="7" height="11" viewBox="0 0 7 11"><path d="M3.5 0.5v10M1 3l2.5-2.5L6 3M1 8l2.5 2.5L6 8" stroke="#fff" fill="none"/></svg></i></div>
<div class="abs bar g3" style="left:486px;top:483px;width:392px"><b>Power from shore</b><span class="sub">7/10 Assets included</span><i class="handle"><svg width="7" height="11" viewBox="0 0 7 11"><path d="M3.5 0.5v10M1 3l2.5-2.5L6 3M1 8l2.5 2.5L6 8" stroke="#fff" fill="none"/></svg></i></div>
<div class="abs bar g4" style="left:569px;top:513px;width:391px"><b>Reduced flaring</b><span class="sub">1/10 Assets included</span><i class="handle"><svg width="7" height="11" viewBox="0 0 7 11"><path d="M3.5 0.5v10M1 3l2.5-2.5L6 3M1 8l2.5 2.5L6 8" stroke="#fff" fill="none"/></svg></i></div>
<div class="abs bar g5" style="left:471px;top:542px;width:391px"><b>Reduced flaring</b><span class="sub">1/10 Assets included</span><i class="handle"><svg width="7" height="11" viewBox="0 0 7 11"><path d="M3.5 0.5v10M1 3l2.5-2.5L6 3M1 8l2.5 2.5L6 8" stroke="#fff" fill="none"/></svg></i></div>
<div class="abs bar g6" style="left:471px;top:572px;width:391px"><b>Reduced flaring</b><span class="sub">1/10 Assets included</span><i class="handle"><svg width="7" height="11" viewBox="0 0 7 11"><path d="M3.5 0.5v10M1 3l2.5-2.5L6 3M1 8l2.5 2.5L6 8" stroke="#fff" fill="none"/></svg></i></div>

<div class="abs" style="left:436px;top:377px;width:1px;height:220px;background:var(--green)"></div>
<div class="abs" style="left:429px;top:370px;width:15px;height:15px;border-radius:50%;background:var(--green)"></div>

<div class="abs volume" role="img" aria-label="Decorative emission volume band"></div>

</body>
</html>
```